Amber Heron Fund Pitch Deck

This is a PowerPoint for use in investor presentations. The copy is written (although it may have small tweaks) and the designer will be responsible for creating a template and some graphical representations inside the presentation.

Note on the logo. Only the Amber Heron should be used, not the text.

```html
<!DOCTYPE html>
<html lang="en">
<head>
<meta charset="utf-8">
<title>Amber Heron Fund Pitch Deck</title>
<link href="https://fonts.googleapis.com/css2?family=Montserrat:wght@400;500;600;700;800&display=swap" rel="stylesheet">
<style>
:root{
  --page:#d2d2d2;
  --ink:#1f2430;
  --body:#2b2f38;
  --blue:#6a87c8;
  --blue-deep:#3a66c4;
  --accent:#4f78d6;
  --rule:#c4c8d0;
  --white:#ffffff;
  --photo-a:#8d9bb0;
  --photo-b:#c9d2dd;
}
*{box-sizing:border-box;margin:0;padding:0}
html,body{width:742px;height:1200px;overflow:hidden}
body{background:var(--page);font-family:"Montserrat",Arial,sans-serif;color:var(--body);position:relative}

.slide{position:absolute;width:340px;height:191px;overflow:hidden;
  background:linear-gradient(125deg,#ffffff 35%,#e9e9e9 70%,#d9d9d9);
  box-shadow:0 6px 10px rgba(0,0,0,.22)}
.slide > *{position:absolute}
.col-left{left:22px}.col-right{left:380px}
.row-1{top:412px}.row-2{top:630px}.row-3{top:848px}

.title-mark{left:4px;top:14px;width:1.6px;height:11px;background:var(--blue)}
.deck-title{left:11px;top:13px;font-size:10.5px;font-weight:700;color:var(--ink)}
.section{font-size:6px;font-weight:600;color:var(--blue)}
.copy{font-size:4.2px;line-height:1.35;color:var(--body)}
.copy p+p{margin-top:3px}
.justify{text-align:justify}

.footer-band{left:0;bottom:0;width:340px;height:8px;background:var(--blue)}
.footer-tab{right:0;bottom:0;width:100px;height:16px;background:var(--blue);clip-path:polygon(12% 0,100% 0,100% 100%,0 100%)}
.page-no{left:12px;bottom:2px;font-size:4px;color:var(--white);font-weight:600}
.footer-brand{right:10px;bottom:8px;font-size:4px;color:var(--white);font-weight:600;white-space:nowrap}
.footer-brand b{font-weight:600;margin-right:4px}

.photo{border-radius:5px;background:linear-gradient(135deg,var(--photo-a),var(--photo-b))}
.avatar{width:41px;height:40px;background:linear-gradient(180deg,#f1f1f1,#d3d3d3)}
.divider{left:7px;width:326px;height:.6px;background:var(--rule)}

.person{font-size:4.2px;line-height:1.35;color:var(--body)}
.person h4{font-size:4.4px;font-weight:400;margin-bottom:2px}
.person h4 b{font-weight:700}
.person ul{list-style:none}
.person li{position:relative;padding-left:5px;margin-bottom:1.6px}
.person li::before{content:"";position:absolute;left:1px;top:1.8px;width:1.2px;height:1.2px;border-radius:50%;background:var(--body)}

.market{font-size:5.6px;line-height:1.5;color:var(--ink);font-weight:400}
.market em{font-style:normal;font-weight:600;color:var(--accent);font-size:6.4px}
.source{left:11px;top:95px;width:318px;height:12px;border-radius:6px;background:var(--blue);color:var(--white);font-size:5.6px;line-height:12px;padding-left:6px;white-space:nowrap}
.source b{font-weight:700}

.steps{left:11px;top:52px;width:318px;height:13px;display:flex}
.steps span{flex:1;color:var(--white);font-size:7px;font-weight:700;text-align:center;line-height:13px}
.step-line{width:.7px;background:#3b4f80}
.step-box{width:42px;border-radius:3px;color:var(--white);font-size:3.2px;line-height:1.3;text-align:center;padding:12px 2px 2px;display:flex;align-items:flex-start;justify-content:center}
.step-icon{width:13px;height:13px;border-radius:50%;background:var(--white);border:1.2px solid currentColor}
.process-note{left:11px;top:164px;width:230px;font-size:3.9px;line-height:1.3;color:var(--ink)}

.cover{position:absolute;left:71px;top:40px;width:600px;height:338px;overflow:hidden;
  background:linear-gradient(125deg,#ffffff 40%,#e4e4e4);box-shadow:0 10px 18px rgba(0,0,0,.25)}
.cover > *{position:absolute}
.cover-photo{left:0;top:0;width:600px;height:190px;background:linear-gradient(160deg,#b7c0cb,#7e8a9c 55%,#9aa6b6)}
.cover-wave{left:0;top:150px;width:600px;height:90px}
.cover-brand{left:0;width:600px;top:208px;text-align:center;font-size:15px;font-weight:700;color:var(--blue);letter-spacing:.5px}
.cover-title{left:0;width:600px;top:246px;text-align:center;font-size:28px;font-weight:800;color:var(--ink);letter-spacing:.5px}
.cover-url{left:0;width:600px;top:284px;display:flex;justify-content:center;align-items:center;gap:8px;font-size:12px;letter-spacing:1.5px;color:#333}
.cover-url i{display:block;width:34px;height:1px;background:#333}
.cover-band{left:0;bottom:0;width:600px;height:8px;background:var(--blue)}
</style>
</head>
<body>

<section class="cover" aria-label="Title slide">
  <div class="cover-photo" role="img" aria-label="Photo of a presenter speaking to colleagues in a bright glass-walled office"></div>
  <svg class="cover-wave" viewBox="0 0 600 90" preserveAspectRatio="none" aria-hidden="true">
    <path d="M0 40 C120 10 200 60 300 34 C400 8 480 50 600 30 L600 90 L0 90 Z" fill="var(--blue)" opacity=".85"/>
    <path d="M0 62 C150 40 220 80 320 56 C420 32 500 66 600 52 L600 90 L0 90 Z" fill="#f4f4f4"/>
  </svg>
  <div class="cover-brand">Amber Heron</div>
  <h1 class="cover-title">PRESENTATION TITLE</h1>
  <div class="cover-url"><i></i>www.amberheron.example<i></i></div>
  <div class="cover-band"></div>
</section>

<section class="slide col-left row-1">
  <div class="title-mark"></div><h2 class="deck-title">Amber Heron Fund</h2>
  <h3 class="section" style="left:11px;top:36px">01. The Edge</h3>
  <div class="copy" style="left:11px;top:52px;width:318px">
    <p>Experience with fund management and asset disposal. Utilizing the clues and hints that borrowers and guarantors leave on the Internet, we can special service assets and collect on them more quickly and maximize return.</p>
    <p>Much of the technology and experience as a team can be attributed to the team's experience at Ambernut. The principals were the management team that came on in March 2020 and grew the business from less than 12,000 PPP loans to more than 800,000.</p>
  </div>
  <h3 class="section" style="left:11px;top:93px">02. The Technology</h3>
  <div class="copy justify" style="left:11px;top:108px;width:170px">
    <p>Most lenders and servicers use Lendara or Servanta and then software like Dunnex for collections.</p>
    <p>These software packages fail to address the most important factors which is to analyze the borrower (and the guarantors) to allow for customized collection plans. We use enhanced skip tracing developed during PPP forgiveness and collection efforts with advanced social media logic.</p>
    <p>Finally, we use evolving algorithms to price and purchase NPL portfolios at the correct price.</p>
  </div>
  <div class="photo" style="left:190px;top:95px;width:139px;height:61px" role="img" aria-label="Photo of a team working together at computer screens in a brick-walled office"></div>
  <div class="footer-tab"></div><div class="footer-band"></div>
  <span class="page-no">01</span>
  <span class="footer-brand"><b>Amber Heron</b>www.amberheron.example</span>
</section>

<section class="slide col-right row-1">
  <div class="title-mark"></div><h2 class="deck-title">Amber Heron Fund</h2>
  <h3 class="section" style="left:11px;top:36px">03. The People</h3>
  <div class="avatar" style="left:11px;top:52px" role="img" aria-label="Profile photo placeholder"></div>
  <div class="person" style="left:60px;top:53px;width:272px">
    <h4><b>Grant Whitfield</b> I Managing Partner, Investment Committee</h4>
    <ul>
      <li>More than 20 years of banking experience with Varnell Ostrom, Ostervale Bank and Kelderane Bank</li>
      <li>Director of Quelmont Capital Management, in less than 5 years, achieved 4x AUM and outsized returns managing distressed asset fund. Developed framework for additional funds.</li>
      <li>CEO of Ambernut.</li>
    </ul>
  </div>
  <div class="divider" style="top:103px"></div>
  <div class="avatar" style="left:11px;top:112px" role="img" aria-label="Profile photo placeholder"></div>
  <div class="person" style="left:60px;top:111px;width:272px">
    <h4><b>Lionel Marsh</b> I Managing Partner, Investment Committee</h4>
    <ul>
      <li>Founder of Orlenta Law in Scottsdale, Arizona which became the first law firm in the country sold to private non-lawyer investors.</li>
      <li>Extensive experience with large transactions (including leading the largest 2017 Arizona transaction on behalf of a client). Known for liquidation sales inside bankruptcy. Speaker at Saguaro Insolvency Institute conference in Las Vegas.</li>
      <li>COO of Wexorin, an early web development company that first implemented a commercially successful e-commerce campaign. Developer of Membrava software suite for Association and Non-Profit Management.</li>
      <li>General Counsel of Ambernut.</li>
    </ul>
  </div>
  <div class="footer-tab"></div><div class="footer-band"></div>
  <span class="page-no">02</span>
  <span class="footer-brand"><b>Amber Heron</b>www.amberheron.example</span>
</section>

<section class="slide col-left row-2">
  <div class="title-mark"></div><h2 class="deck-title">Amber Heron Fund</h2>
  <h3 class="section" style="left:11px;top:36px">03. The People</h3>
  <div class="avatar" style="left:11px;top:52px" role="img" aria-label="Profile photo placeholder"></div>
  <div class="person" style="left:60px;top:54px;width:272px">
    <h4><b>Owen Castell</b> I Investment Committee</h4>
    <ul>
      <li>CEO of Quarvel Impact Corp. (OTCQB: QRVL))</li>
      <li>CEO, Talvibank</li>
      <li>Director, Nerevo Bank</li>
      <li>Member, Ostrelle Corporate Directors Association</li>
    </ul>
  </div>
  <div class="divider" style="top:103px"></div>
  <div class="avatar" style="left:11px;top:112px" role="img" aria-label="Profile photo placeholder"></div>
  <div class="person" style="left:60px;top:110px;width:272px">
    <h4><b>Peter Valcourt</b> I Director of Credit Analytics.</h4>
    <ul>
      <li>Product and data specialist with more than 15 years technology and startup experience.</li>
      <li>Founded Pellanor Communications, which combined email and chat for customer success professionals. Raised $5 million capital and had more than 40,000 users.</li>
      <li>Led advertising products at Quillora and grew from $7 million to $45 million in revenue over 5 years.</li>
      <li>Advisory Board member with well-known venture capital firm.</li>
      <li>VP, Products, Ambernut.</li>
    </ul>
  </div>
  <div class="footer-tab"></div><div class="footer-band"></div>
  <span class="page-no">03</span>
  <span class="footer-brand"><b>Amber Heron</b>www.amberheron.example</span>
</section>

<section class="slide col-right row-2">
  <div class="title-mark"></div><h2 class="deck-title">Amber Heron Fund</h2>
  <h3 class="section" style="left:11px;top:36px">03. The People</h3>
  <div class="avatar" style="left:11px;top:52px" role="img" aria-label="Profile photo placeholder"></div>
  <div class="person" style="left:60px;top:54px;width:272px">
    <h4><b>Rory Denholm</b> I Chief Operating Officer</h4>
    <ul>
      <li>Management Consultant at Dorvane &amp; Company and Tessarine</li>
      <li>Founder of two companies that grew to more than 1,000 employees.</li>
      <li>COO of Ambernut.</li>
    </ul>
  </div>
  <div class="photo" style="left:11px;top:102px;width:318px;height:61px;background:linear-gradient(100deg,#6f87b8,#b9c7dc 45%,#5f79ad)" role="img" aria-label="Photo of a group of colleagues in discussion in a modern office"></div>
  <div class="footer-tab"></div><div class="footer-band"></div>
  <span class="page-no">04</span>
  <span class="footer-brand"><b>Amber Heron</b>www.amberheron.example</span>
</section>

<section class="slide col-left row-3">
  <div class="title-mark"></div><h2 class="deck-title">Amber Heron Fund</h2>
  <h3 class="section" style="left:11px;top:36px">04. The Market</h3>
  <p class="market" style="left:11px;top:52px;width:318px">The commercial lending market size was valued at <em>$8,823.53</em> billion in 2020, and is projected to reach <em>$29,379.83</em> billion by 2030, growing at a CAGR of <em>13.1%</em> from 2021 to 2030.</p>
  <div class="source"><b>Source:</b> https://www.quorvane-research.example/commercial-lending-market</div>
  <p class="market" style="left:11px;top:120px;width:135px">The credit cycle is entering into a period of rising interest rates and corresponding defaults. The fund seeks to take advantage of that emerging opportunity.</p>
  <div class="photo" style="left:153px;top:115px;width:176px;height:52px;border-radius:0;background:linear-gradient(135deg,#dfe6f2,#9fb6e0 50%,#eef1f6)" role="img" aria-label="Photo of printed financial charts beside a keyboard"></div>
  <div class="footer-tab"></div><div class="footer-band"></div>
  <span class="page-no">05</span>
  <span class="footer-brand"><b>Amber Heron</b>www.amberheron.example</span>
</section>

<section class="slide col-right row-3">
  <div class="title-mark"></div><h2 class="deck-title">Amber Heron Fund</h2>
  <h3 class="section" style="left:11px;top:36px">05. Our Process</h3>
  <div class="steps">
    <span style="background:#3a66c4">A</span><span style="background:#3d74dc">B</span><span style="background:#3b7fe6">C</span><span style="background:#3a6bd0">D</span><span style="background:#4a86e8">E</span><span style="background:#5a8fe6">F</span><span style="background:#6a8ac8">G</span>
  </div>

  <div class="step-line" style="left:33.5px;top:65px;height:46px"></div>
  <div class="step-line" style="left:79px;top:65px;height:24px"></div>
  <div class="step-line" style="left:124.4px;top:65px;height:57px"></div>
  <div class="step-line" style="left:169.8px;top:65px;height:35px"></div>
  <div class="step-line" style="left:215.2px;top:65px;height:51px"></div>
  <div class="step-line" style="left:260.6px;top:65px;height:19px"></div>
  <div class="step-line" style="left:306px;top:65px;height:54px"></div>

  <div class="step-box" style="left:12.5px;top:105px;height:55px;background:#3a66c4;padding-top:18px">Work with our lender customers on their non-performing loan portfolio.</div>
  <div class="step-box" style="left:58px;top:83px;height:40px;background:#3d74dc">Purchase participation in non-performing loans</div>
  <div class="step-box" style="left:103.4px;top:116px;height:41px;background:#3b7fe6">Provide special servicing in compliance with bank's servicing criteria.</div>
  <div class="step-box" style="left:148.8px;top:94px;height:40px;background:#3a6bd0;padding-top:15px">Provide bank access to NPL platform.</div>
  <div class="step-box" style="left:194.2px;top:110px;height:42px;background:#4a86e8">Maintain first right of refusal to purchase loan using proprietary algorithm.</div>
  <div class="step-box" style="left:239.6px;top:78px;height:41px;background:#5a8fe6;padding-top:14px">Internal servicing standards.</div>
  <div class="step-box" style="left:285px;top:113px;height:40px;background:#6a8ac8;padding-top:14px">Liquidation, when necessary.</div>

  <div class="step-icon" style="left:27px;top:105px;color:#3a66c4"></div>
  <div class="step-icon" style="left:72.5px;top:77px;color:#3d74dc"></div>
  <div class="step-icon" style="left:117.9px;top:110px;color:#3b7fe6"></div>
  <div class="step-icon" style="left:163.3px;top:88px;color:#3a6bd0"></div>
  <div class="step-icon" style="left:208.7px;top:104px;color:#4a86e8"></div>
  <div class="step-icon" style="left:254.1px;top:72px;color:#5a8fe6"></div>
  <div class="step-icon" style="left:299.5px;top:107px;color:#6a8ac8"></div>

  <p class="process-note">Initially partner with licensed collection agencies to supplement our in-house abilities (and comply with regulatory requirements). Potential to acquire and bring completely in-house.</p>
  <div class="footer-tab"></div><div class="footer-band"></div>
  <span class="page-no">06</span>
  <span class="footer-brand"><b>Amber Heron</b>www.amberheron.example</span>
</section>

</body>
</html>
```